Design a Certificate of Training that we will distribute to our clients after they complete a training with our business. You will incorporate our logo, business name: MARBLE Steps Tutors & Training and our tag line: Forever Keen to Learn Beside You. The colors to use are as follows: Brown #R53 G36 B23. Yellow: R248 G231 B6. Blue Green: R33 G201 B188. Have fun and be creative. See logo in the attachment.

Add:
This certifies that (add a mock name) Ned Pell has successfully completed the MARBLE Steps Training Course

```html
<!DOCTYPE html>
<html lang="en">
<head>
<meta charset="utf-8">
<title>Certificate of Training – MARBLE Steps</title>
<link rel="stylesheet" href="https://fonts.googleapis.com/css2?family=Cinzel:wght@400&family=Source+Sans+3:wght@400;600;700&display=swap">
<style>
  :root {
    --brown: #352417;
    --yellow: #f8e706;
    --teal: #21c9bc;
    --green: #3fd61c;
    --ink: #2b2b2b;
    --paper: #ffffff;
  }
  html, body {
    margin: 0;
    padding: 0;
    width: 1200px;
    height: 836px;
    overflow: hidden;
    background: var(--paper);
  }
  .certificate {
    position: relative;
    width: 1200px;
    height: 836px;
    background: var(--paper);
    font-family: "Source Sans 3", "Helvetica Neue", Arial, sans-serif;
    color: var(--ink);
  }
  .certificate__frame {
    position: absolute;
    inset: 0;
  }
  .brand {
    position: absolute;
    left: 46px;
    top: 82px;
    display: flex;
    align-items: center;
    gap: 14px;
  }
  .brand__square {
    width: 40px;
    height: 40px;
    background: var(--yellow);
  }
  .brand__name {
    font-weight: 700;
    font-size: 31px;
    color: var(--brown);
    letter-spacing: 0.2px;
  }
  .content {
    position: absolute;
    left: 540px;
    width: 394px;
    top: 0;
    height: 100%;
    text-align: center;
  }
  .content > * {
    position: absolute;
    left: -200px;
    right: -200px;
    margin: 0;
    white-space: nowrap;
  }
  .title {
    top: 70px;
    font-weight: 700;
    font-size: 58px;
    letter-spacing: -1.2px;
    color: var(--brown);
    transform: scaleX(0.9);
  }
  .awarded {
    top: 166px;
    font-size: 22px;
    color: var(--green);
  }
  .recipient {
    top: 236px;
    font-family: "Cinzel", "Trajan Pro", Georgia, serif;
    font-size: 56px;
    color: var(--teal);
    letter-spacing: 1px;
  }
  .completed {
    top: 332px;
    font-size: 26px;
    color: var(--green);
  }
  .course {
    top: 382px;
    font-size: 32px;
    color: var(--ink);
  }
  .date {
    top: 425px;
    font-size: 22px;
    color: var(--teal);
    word-spacing: 3px;
  }
  .signature-label {
    top: 641px;
    font-size: 28px;
    color: var(--teal);
  }
  .tagline {
    top: 730px;
    font-size: 28px;
    color: var(--ink);
  }
</style>
</head>
<body>
  <main class="certificate">
    <svg class="certificate__frame" width="1200" height="836" viewBox="0 0 1200 836" aria-hidden="true">
      <!-- side panel -->
      <path d="M0 0 H405 C335 60 318 190 360 300 C410 430 420 600 242 836 H0 Z" fill="var(--teal)"/>
      <!-- frame rules -->
      <line x1="408" y1="45" x2="1100" y2="45" stroke="var(--teal)" stroke-width="3"/>
      <line x1="250" y1="793" x2="1100" y2="793" stroke="var(--teal)" stroke-width="3"/>
      <!-- corner squares -->
      <rect x="1100" y="0" width="45" height="45" fill="var(--teal)"/>
      <rect x="1154" y="0" width="46" height="45" fill="var(--green)"/>
      <rect x="1154" y="52" width="46" height="45" fill="var(--brown)"/>
      <rect x="1154" y="741" width="46" height="45" fill="var(--brown)"/>
      <rect x="1100" y="795" width="45" height="41" fill="var(--teal)"/>
      <rect x="1154" y="795" width="46" height="41" fill="var(--green)"/>
      <!-- recipient and signature rules -->
      <line x1="573" y1="313" x2="904" y2="313" stroke="var(--teal)" stroke-width="2"/>
      <line x1="570" y1="628" x2="904" y2="628" stroke="var(--teal)" stroke-width="2"/>
    </svg>

    <svg style="position:absolute;left:118px;top:413px" width="220" height="220" viewBox="0 0 220 220" role="img" aria-label="Brand mark area">
      <circle cx="110" cy="110" r="110" fill="var(--brown)"/>
    </svg>

    <header class="brand">
      <span class="brand__square" aria-hidden="true"></span>
      <span class="brand__name">MARBLE Steps</span>
    </header>

    <section class="content">
      <h1 class="title">CERTIFICATE OF TRAINING</h1>
      <p class="awarded">AWARDED TO</p>
      <p class="recipient">Ned Pell</p>
      <p class="completed">Who has successfully completed the</p>
      <p class="course">MARBLE Steps Training Course</p>
      <p class="date">Date &nbsp;|&nbsp; January 02, 2018</p>
      <p class="signature-label">Authorized signatures</p>
      <p class="tagline">Forever Keen to Learn Beside You</p>
    </section>
  </main>
</body>
</html>
```